New Zealand health product business needs website designed

A website is required for a business that sells New Zealand made products, namely products like infant formula, health products such as NZ honey, supplements, skincare products etc. This is purely an informative website that will introduce the all the different types of products the business has to offer. The target audience will the the Chinese market. The logo is a calligraphy style font in colours 78b643 and 313542 (logo is still being finalised at the moment) so a colour theme to match would be great.

It is crucial that the design communicates the beautiful nature of New Zealand, non-polluted environments, with emphasis on pure, natural and cleaniness.
Updates

A website that I quite like is http://www.frostvalegelato.co.nz

Information is easy to find, layout is nice and clear.                          

Hi all, I have now uploaded a logo for the business "Tidal Basket", please note that this is yet to be finalized however I expect it to be minor changes so please ensure the website theme and colour use go well with the logo. 

There are three scenery images uploaded, designs with any one of them used is fine whichever works better with your design.  Only one image is required on the website, no sliding effects for this.

Also just to clarify my requirements further.  The developer can use HTML, PHP, Javascript, CSS for coding, preferably to have the images cut and a pdf guide provided for things like alignment and sizing etc.

The menu items are Home / Our story / Product outline / Brands / Contact us
Designs are required for all these.  Within the product outline page, the subcategories are -
Infant formulas
Baby supplements
Toddlers products
Honey
Beauty products
Mens supplements
Womens supplements
Health products
Others

   

Target Market(s)

China based customers looking for quality products from New Zealand.

Industry/Entity Type

Health

Requirements
Must have
• clear menu bar in home page, the four main menu items are -
Our story
Product outline
Brands
Contact us
Nice to have
• Space for a large scenery photo in the home page

```html
<!DOCTYPE html>
<html lang="en">
<head>
<meta charset="utf-8">
<title>Tidal Basket</title>
<link rel="stylesheet" href="https://fonts.googleapis.com/css2?family=Questrial&family=Arimo:wght@400&display=swap">
<style>
  :root {
    --page-bg: #f4f4ef;
    --white: #ffffff;
    --green: #4f9a2f;
    --brand-green: #78b643;
    --dark: #313542;
    --heading: #2b2b2b;
    --muted: #8c8c8c;
    --soft: #a9a9a9;
    --rule: #dcdcd6;
    --rule-light: #e8e8e4;
  }
  * { margin: 0; padding: 0; box-sizing: border-box; }
  html, body {
    width: 1200px; height: 1000px; overflow: hidden;
    background: var(--page-bg);
    font-family: "Arimo", Arial, sans-serif;
  }
  .site { position: relative; width: 1200px; height: 1000px; }

  .site-header { position: absolute; top: 0; left: 0; width: 1200px; height: 107px; }
  .brand {
    position: absolute; left: 163px; top: 22px;
    font-family: "Questrial", sans-serif;
    font-size: 50px; line-height: 60px; color: var(--brand-green);
    letter-spacing: -0.5px;
  }
  .contact-block {
    position: absolute; right: 213px; top: 24px; text-align: right;
    color: var(--muted); font-size: 11px; line-height: 12px;
  }
  .contact-block h2 {
    font-weight: 400; font-size: 15px; color: #6f6f6f; margin-bottom: 13px;
  }

  .main-nav {
    position: absolute; top: 107px; left: 0; width: 1200px; height: 44px;
    background: var(--white);
    border-top: 1px solid var(--rule); border-bottom: 1px solid var(--rule);
  }
  .main-nav ul { list-style: none; display: flex; position: absolute; left: 163px; top: 0; height: 42px; align-items: center; }
  .main-nav li {
    font-family: "Questrial", sans-serif; font-size: 14px; color: var(--green);
    padding: 0 16px; border-left: 1px solid var(--rule-light); line-height: 18px;
  }
  .main-nav li:first-child { padding-left: 0; padding-right: 46px; border-left: 0; color: var(--heading); }
  .main-nav li:nth-child(2) { padding-left: 21px; padding-right: 18px; }

  .breadcrumb {
    position: absolute; left: 163px; top: 168px;
    font-size: 10px; color: var(--green);
  }
  .breadcrumb .crumb-home { text-decoration: underline; }

  .hero {
    position: absolute; top: 198px; left: 0; width: 1200px; height: 464px;
    background:
      linear-gradient(180deg,
        #c9ccca 0%, #6f7474 10%, #8f8a6e 20%, #b39a4d 32%, #6b6a45 44%,
        #b59a5a 50%, #a07a3c 60%, #6e5a3a 70%, #c8c6bd 82%, #e4e6e6 100%);
    box-shadow: 0 6px 10px rgba(0,0,0,0.12);
  }

  .products {
    position: absolute; left: 162px; top: 703px; width: 825px; height: 237px;
    background: var(--white); border: 1px solid #e4e4df;
  }
  .products-head {
    position: absolute; left: 15px; right: 15px; top: 0; height: 43px;
    border-bottom: 1px solid var(--rule-light);
  }
  .products-head h2 {
    position: absolute; left: 0; top: 20px;
    font-weight: 400; font-size: 15px; color: var(--heading);
  }
  .pager { position: absolute; right: 1px; top: 20px; display: flex; gap: 5px; }
  .pager span {
    width: 16px; height: 16px; font-size: 9px; line-height: 16px; text-align: center; color: var(--white);
  }
  .pager .prev { background: #dcdcdc; }
  .pager .next { background: var(--green); }

  .product-list { position: absolute; top: 60px; left: 0; width: 825px; height: 145px; }
  .product {
    position: absolute; top: 0; height: 142px; padding-top: 6px;
  }
  .product + .product { border-left: 1px solid var(--rule-light); }
  .product h3 { font-weight: 400; font-size: 11px; color: #8a8a8a; margin-bottom: 14px; }
  .product p { font-size: 9.5px; line-height: 14.6px; color: var(--soft); width: 168px; }
  .product .read-more { display: block; margin-top: 19px; font-size: 9.5px; color: var(--green); padding-left: 2px; }

  .site-footer {
    position: absolute; left: 162px; top: 959px; width: 825px; height: 41px;
    border-top: 1px solid var(--rule);
  }
  .social { position: absolute; left: 1px; top: 6px; display: flex; gap: 9px; }
  .social span {
    width: 21px; height: 21px; border: 1px solid #cfcfca; border-radius: 3px; background: var(--white);
  }
  .copyright { position: absolute; right: 0; top: 10px; font-size: 8.5px; color: var(--muted); }
</style>
</head>
<body>
<div class="site">
  <header class="site-header">
    <div class="brand">Tidal Basket</div>
    <address class="contact-block" style="font-style:normal">
      <h2>Contact Us:</h2>
      #234, Tidal Basket, UK<br>
      Example of address goes here<br>
      Call: 1234 567<br>
      info@example.com
    </address>
  </header>

  <nav class="main-nav">
    <ul>
      <li>Home</li>
      <li>Our Story</li>
      <li>Product Outline</li>
      <li>Brands</li>
      <li>Contact Us</li>
    </ul>
  </nav>

  <div class="breadcrumb"><span class="crumb-home">Home </span>&gt; Bredscrum Goes Here</div>

  <div class="hero" role="img" aria-label="New Zealand lake landscape with golden autumn trees, cloud-capped mountains and their reflection in still water"></div>

  <section class="products">
    <div class="products-head">
      <h2>Products</h2>
      <div class="pager"><span class="prev">&lt;</span><span class="next">&gt;</span></div>
    </div>
    <div class="product-list">
      <article class="product" style="left:18px;width:180px">
        <h3>Infant formulas</h3>
        <p>Lorem Ipsum is simply dummy text of the printing and typesetting industry. Lorem Ipsum has been the industry's standard</p>
        <span class="read-more">read more..</span>
      </article>
      <article class="product" style="left:197px;width:210px;padding-left:20px">
        <h3>Baby supplements</h3>
        <p>Lorem Ipsum is simply dummy text of the printing and typesetting industry. Lorem Ipsum has been the industry's standard</p>
        <span class="read-more">read more..</span>
      </article>
      <article class="product" style="left:404px;width:214px;padding-left:23px">
        <h3>Toddlers products</h3>
        <p>Lorem Ipsum is simply dummy text of the printing and typesetting industry. Lorem Ipsum has been the industry's standard</p>
        <span class="read-more">read more..</span>
      </article>
      <article class="product" style="left:616px;width:200px;padding-left:27px">
        <h3>Honey</h3>
        <p>Lorem Ipsum is simply dummy text of the printing and typesetting industry. Lorem Ipsum has been the industry's standard</p>
        <span class="read-more">read more..</span>
      </article>
    </div>
  </section>

  <footer class="site-footer">
    <div class="social" aria-label="Social links"><span></span><span></span><span></span><span></span></div>
    <div class="copyright">Copyright 2013 All Right Reserved</div>
  </footer>
</div>
</body>
</html>
```